Creative, fresh business card design for Brindlecrest Linings

We need a fresh, creative business card design for Brindlecrest Linings. We are the manufacturer of Brindlecrest Linings in Australia. Wall panels are 2400 x 1200mm panels made from MDF and feature 3D patterns on the face of the panel. The colours to be used are green, silver/grey and white RGB
Red 187
Green 207
Blue 65.

An idea is to possibly use a watermark of one of our designs as a background (like on the "Lattice" design on the left hand side of page 2 of our brochure).

Target Market(s)

Interior designers, architects, builders and home renovators

Industry/Entity Type

Business

Contact Information for Business Card

Details to go on the card are:
Our logo (attached),
Slogan: "Decorative panels for interiors and exteriors",
Contact name,
Position,
Mobile phone number,
Business address,
Business phone,
Business fax,
Website and
Email address.

I have attached a few images of our panels and our brochure for reference.

The colours of the business card should feature our logo colours which are: RGB
Red 187
Green 207
Blue 65

Requirements
Must have
• Very modern fonts and design. Some of the designs shown especially the "Weave" design which is a popular design.
Nice to have
• Creative but simple design. Very contemporary.
Should not have
• Anything ornate or old fashioned.

```html
<!DOCTYPE html>
<html lang="en">
<head>
<meta charset="utf-8">
<title>Brindlecrest Linings – Business Card</title>
<link rel="stylesheet" href="https://fonts.googleapis.com/css2?family=Roboto:wght@300;400;700&display=swap">
<style>
  :root {
    --brand-green: rgb(187, 207, 65);
    --frame-grey: #a7a9ac;
    --text-grey: #8a8c8f;
    --pattern-light: #f2f2f3;
    --pattern-mid: #d9dadb;
    --paper: #ffffff;
  }
  html, body {
    margin: 0;
    padding: 0;
    width: 1200px;
    height: 1200px;
    overflow: hidden;
    background: var(--paper);
    font-family: "Roboto", Arial, sans-serif;
    color: var(--text-grey);
  }
  .sheet { position: relative; width: 1200px; height: 1200px; }
  .card {
    position: absolute;
    left: 208px;
    width: 770px;
    height: 498px;
    box-sizing: border-box;
    border: 3px solid var(--frame-grey);
    background: var(--paper);
    overflow: hidden;
  }
  .card--front { top: 60px; }
  .card--back { top: 634px; }
  .pattern { position: absolute; inset: 0; width: 100%; height: 100%; }

  /* Front */
  .brand-lockup {
    position: absolute;
    left: 340px;
    top: 238px;
    display: flex;
    align-items: center;
    gap: 14px;
  }
  .brand-lockup__square {
    width: 34px; height: 34px;
    background: var(--brand-green);
  }
  .brand-lockup__name {
    font-weight: 300;
    font-size: 31px;
    color: var(--text-grey);
    white-space: nowrap;
  }
  .tagline {
    position: absolute;
    left: 384px;
    top: 317px;
    width: 300px;
    text-align: center;
    font-weight: 400;
    font-size: 18px;
    line-height: 22px;
    letter-spacing: 4px;
    color: var(--text-grey);
  }

  /* Back */
  .name-band {
    position: absolute;
    left: 48px;
    top: 49px;
    height: 70px;
    padding: 0 26px;
    display: flex;
    align-items: center;
    background: var(--brand-green);
    color: var(--paper);
    font-weight: 300;
    font-size: 40px;
    white-space: nowrap;
  }
  .person { position: absolute; left: 75px; top: 153px; font-size: 23px; line-height: 29px; }
  .person__name { font-weight: 700; margin: 0; }
  .person__role { font-weight: 300; margin: 0; }
  .contact {
    position: absolute;
    left: 75px;
    top: 239px;
    border-collapse: collapse;
    font-weight: 300;
    font-size: 23px;
    line-height: 29px;
  }
  .contact th { font-weight: 300; text-align: left; padding: 0; width: 149px; }
  .contact td { padding: 0; white-space: nowrap; }
  .online {
    position: absolute;
    left: 75px;
    top: 383px;
    font-weight: 700;
    font-size: 22px;
    line-height: 29px;
    color: var(--brand-green);
  }
  .online p { margin: 0; }
</style>
</head>
<body>
<main class="sheet">
  <section class="card card--front">
    <svg class="pattern" viewBox="0 0 770 498" role="img" aria-label="Pyramid wall panel pattern in soft greys">
      <defs>
        <linearGradient id="frontPanel" x1="0" y1="0" x2="1" y2="1">
          <stop offset="0" stop-color="var(--pattern-light)"/>
          <stop offset="1" stop-color="var(--pattern-mid)"/>
        </linearGradient>
      </defs>
      <polygon points="0,0 98,0 347,498 0,498" fill="url(#frontPanel)"/>
    </svg>
    <div class="brand-lockup">
      <span class="brand-lockup__square"></span>
      <span class="brand-lockup__name">Brindlecrest Linings</span>
    </div>
    <p class="tagline">decorative panels for interiors &amp; landscapes</p>
  </section>

  <section class="card card--back">
    <svg class="pattern" viewBox="0 0 770 498" role="img" aria-label="Faint pyramid wall panel pattern">
      <defs>
        <linearGradient id="backPanel" x1="1" y1="0" x2="0" y2="1">
          <stop offset="0" stop-color="#ececed"/>
          <stop offset="1" stop-color="#f7f7f7"/>
        </linearGradient>
      </defs>
      <polygon points="672,0 770,0 770,498 424,498" fill="url(#backPanel)"/>
    </svg>
    <div class="name-band">Brindlecrest Linings</div>
    <div class="person">
      <p class="person__name">Mara Ellison</p>
      <p class="person__role">Occupation</p>
    </div>
    <table class="contact">
      <tr><th>Mobile:</th><td>0491 570 183</td></tr>
      <tr><th>Address:</th><td>14 Kestrel Lane, Alder Vale, NSW 2190</td></tr>
      <tr><th>Phone:</th><td>02 5550 4222</td></tr>
      <tr><th>Fax:</th><td>02 5550 4777</td></tr>
    </table>
    <div class="online">
      <p>sales@brindlecrestlinings.com.au</p>
      <p>www.brindlecrestlinings.com.au</p>
    </div>
  </section>
</main>
</body>
</html>
```